Singer/Songwriter Artist Promotion Website

***DO NOT CONTACT ME PRIVATELY***

I need a fresh, exciting, upbeat-looking site. The purpose of our business is to genuinely promote unknown, unsigned music artists. The sight initially needs a feel slanted toward Country Music.

DESIGN
The website design should be similar to this site;
https://www.tunovaleo.com

For the design, make it follow a linear flow of sections/blocks. We don't want a complex design with objects/images in random parts of the page, but rather section "blocks" of content.

I need 5 pages designed;
Home
FAQ
Our Staff
"Launch Your Music" This page is more complex. This page needs to display a questionnaire that can be filled out. This page will need to be able to capture and process payments. There needs to be a way to attach files for upload.
"Artist Profiles" - > A template page that will be used for multiple artists. It will show the artist/musician information

Design/Colors
I want colors that are attractive, professional but exciting. I’m looking for tasteful, interesting, eye-catching, not boring.

Taglines;
Name: “Balladcraft Airwave Circle”
Tagline: “All Original Artists-All Original Country
24/7, Commercial Free, All The Time”

LOGO DESIGN
- See attached basic logo
Balladcraft Airwave Circle
BAC
Base design off of attached logo. I’d like the "Balladcraft Airwave Circle" to be Colorful. Attention getting. Possibly showing some movement. Maybe a gradient.

Target Market(s)

Independent Musicians

Industry/Entity Type

Songwriting, Music Promotion, Radio Network

Number of Pages Required

5+ page

Colors
00AB8E
00BBA5
67D7C9
C6EFE9
E9F9F6

```html
<!DOCTYPE html>
<html lang="en">
<head>
<meta charset="utf-8">
<title>Balladcraft Airwave Circle</title>
<link href="https://fonts.googleapis.com/css2?family=Oswald:wght@300;400;500;600&family=Lato:wght@400;700&display=swap" rel="stylesheet">
<style>
:root{
  --navy:#1b2237;
  --navy-deep:#161c2e;
  --blue:#1a35d6;
  --white:#ffffff;
  --ink:#1c1f2a;
  --muted:#4a4f5c;
  --grey-band:#eceef2;
  --step-yellow:#f5cf16;
  --step-orange:#e0521b;
  --step-purple:#4b2a8e;
  --caption:#8b91a3;
}
*{box-sizing:border-box;margin:0;padding:0}
html,body{width:1200px;height:4000px;overflow:hidden}
body{font-family:"Lato",sans-serif;color:var(--ink);background:var(--white);position:relative}
section,header,footer{position:absolute;left:0;width:1200px}
.heading{font-family:"Oswald",sans-serif;font-weight:500;text-transform:uppercase;letter-spacing:.5px}
.btn{display:inline-flex;align-items:center;gap:8px;background:var(--blue);color:var(--white);font-family:"Oswald",sans-serif;font-weight:500;font-size:14px;letter-spacing:.5px;text-transform:uppercase;border-radius:3px;padding:0 26px;height:42px}
.brand{font-family:"Oswald",sans-serif;font-weight:600;color:var(--white);font-size:56px;line-height:1;letter-spacing:2px;display:flex;align-items:center;gap:12px}
.brand .mark{width:14px;height:14px;background:var(--white);border-radius:50%}

/* Hero */
.hero{top:0;height:581px;background:linear-gradient(110deg,#3a2a1c 0%,#7a5330 35%,#c89468 65%,#e6c4a2 100%)}
.hero .brand{position:absolute;left:174px;top:16px}
.nav{position:absolute;left:430px;top:33px;display:flex;gap:32px;font-family:"Oswald",sans-serif;font-size:13px;color:var(--white);text-transform:uppercase}
.social{display:flex;gap:18px}
.social span{width:14px;height:14px;border:2px solid var(--white);border-radius:50%;display:block}
.hero .social{position:absolute;left:910px;top:35px}
.hero-title{position:absolute;left:174px;top:210px;color:var(--white);font-size:48px;line-height:58px;width:560px}
.hero-tag{position:absolute;left:174px;top:333px;color:var(--white);font-family:"Oswald",sans-serif;font-size:19px;letter-spacing:6px}
.hero .btn{position:absolute;left:174px;top:382px;height:44px}
.dots{position:absolute;left:562px;top:524px;display:flex;gap:9px}
.dots span{width:13px;height:13px;border:1.5px solid var(--white);border-radius:50%}
.dots span.on{background:var(--white)}

/* Welcome */
.welcome{top:581px;height:469px}
.welcome-art{position:absolute;left:144px;top:56px;width:482px;height:256px;background:linear-gradient(90deg,#1b1b1b 0%,#3a3a3a 55%,#b98a66 100%);border-radius:4px}
.welcome-text{position:absolute;left:650px;top:85px;width:420px}
.eyebrow{font-family:"Oswald",sans-serif;color:var(--blue);font-size:17px;line-height:20px;letter-spacing:8px}
.welcome-title{font-size:40px;line-height:56px;margin-top:8px;font-weight:600}
.welcome-title span{font-weight:300}
.welcome-text p.lead{font-size:14.5px;line-height:26px;margin-top:16px;color:var(--muted);width:390px}
.welcome-text .btn{display:flex;width:fit-content;margin-top:16px}

/* Partners */
.partners{top:1050px;height:300px;background:var(--grey-band)}
.partners h2{text-align:center;padding-top:52px;font-size:46px;font-weight:300}
.partners h2 b{font-weight:600}
.partner-row{position:absolute;left:174px;top:138px;width:852px;display:flex;justify-content:space-between}
.partner-row span{width:84px;height:84px;background:#8e929b;border-radius:8px;opacity:.75}
.partner-row span.round{border-radius:50%}

/* Exposure */
.exposure{top:1350px;height:538px;background:radial-gradient(circle at 78% 40%,#33406a 0%,var(--navy) 55%)}
.exposure-art{position:absolute;left:668px;top:-41px;width:404px;height:624px;background:linear-gradient(180deg,#7a5236 0%,#3a3a3a 50%,#2a2622 100%);border-radius:40% 40% 6px 6px}
.exposure h2{position:absolute;left:172px;top:80px;color:var(--white);font-size:46px;line-height:56px;font-weight:600}
.exposure h2 sup{font-size:22px}
.exposure .sub{position:absolute;left:172px;top:206px;color:var(--white);font-family:"Oswald",sans-serif;font-size:25px;font-weight:300}
.exposure .sub b{font-weight:600}
.points{position:absolute;left:172px;top:270px;width:480px;list-style:none;color:#dfe2ea;font-size:15px;line-height:25px}
.points li{position:relative;padding-left:19px;margin-bottom:9px}
.points li::before{content:"";position:absolute;left:0;top:9px;width:8px;height:8px;border-radius:50%;background:#3d5bff}

/* How it works */
.how{top:1888px;height:761px}
.how h2{text-align:center;padding-top:68px;font-size:48px;font-weight:600}
.steps{position:absolute;left:174px;top:142px;display:flex;gap:79px}
.step{position:relative;width:232px;height:540px}
.step-accent{position:absolute;right:-2px;top:250px;width:36px;height:290px;border-radius:30px 0 0 0}
.step-card{position:absolute;left:0;top:0;width:200px;height:480px;background:var(--white);border-radius:100px 100px 28px 0;box-shadow:0 2px 12px rgba(0,0,0,.12);padding:150px 10px 0;text-align:center;font-size:12.5px;line-height:20.5px;color:var(--muted)}
.step-icon{position:absolute;left:40px;top:20px;width:120px;height:120px;border-radius:50%;background:radial-gradient(circle at 40% 35%,#ffffff 0%,#e4e6ea 70%,#c9ccd2 100%);box-shadow:0 4px 10px rgba(0,0,0,.15)}
.step-tab{position:absolute;left:90px;top:478px;width:142px;height:62px;border-radius:30px 0 0 0;color:var(--white);font-family:"Oswald",sans-serif;font-size:18px;font-weight:500;display:flex;align-items:center;justify-content:center}
.step-tab b{font-size:24px;margin-left:4px}
.step.one .step-accent,.step.one .step-tab{background:linear-gradient(180deg,#f7ea4a,var(--step-yellow))}
.step.two .step-accent,.step.two .step-tab{background:linear-gradient(180deg,#e2391d,var(--step-orange))}
.step.three .step-accent,.step.three .step-tab{background:linear-gradient(180deg,#5a36a8,var(--step-purple))}

/* Artists */
.artists{top:2649px;height:597px;background:var(--navy)}
.artists h2{text-align:center;color:var(--white);padding-top:58px;font-size:48px;font-weight:600}
.artist-row{position:absolute;left:172px;top:126px;display:flex;gap:26px}
.artist{width:268px;background:var(--navy-deep)}
.artist-photo{height:301px}
.artist:nth-child(1) .artist-photo{background:linear-gradient(180deg,#8ea6bf,#4f6e93)}
.artist:nth-child(2) .artist-photo{background:linear-gradient(180deg,#6f6a5e,#c4b49a)}
.artist:nth-child(3) .artist-photo{background:linear-gradient(180deg,#b9b7b4,#5a4436)}
.artist-info{height:81px;text-align:center;padding-top:18px}
.artist-info h3{color:var(--white);font-size:17px;font-weight:700}
.artist-info p{color:var(--caption);font-size:13px;margin-top:2px}

/* FAQ */
.faq{top:3246px;height:366px}
.faq h2{text-align:center;padding-top:52px;font-size:48px;font-weight:600}
.faq-grid{position:absolute;left:172px;top:127px;width:856px;display:grid;grid-template-columns:417px 417px;column-gap:22px;row-gap:7px}
.faq-item{background:var(--navy-deep);color:var(--white);font-size:14px;line-height:16px;height:40px;border-radius:2px;padding:0 44px 0 12px;display:flex;align-items:center;position:relative}
.faq-item::after{content:"";position:absolute;right:12px;top:12px;width:16px;height:16px;border-radius:50%;background:var(--white)}
.faq-item::before{content:"";position:absolute;right:17px;top:16px;border-left:7px solid var(--navy-deep);border-top:4px solid transparent;border-bottom:4px solid transparent;z-index:1}

/* Footer */
.footer{top:3612px;height:388px;background:var(--navy)}
.footer .brand{position:absolute;left:174px;top:118px;font-size:60px}
.footer .social{position:absolute;left:174px;top:228px;gap:30px}
.divider{position:absolute;top:88px;width:1px;height:266px;background:#3b4460}
.divider::after{content:"";position:absolute;left:-2px;top:70px;width:5px;height:30px;background:var(--white)}
.col-title{font-family:"Oswald",sans-serif;color:var(--white);font-size:16px;font-weight:500}
.quick{position:absolute;left:517px;top:82px}
.quick ul{list-style:none;margin-top:16px}
.quick li{color:#c9cdd8;font-size:14px;height:37.5px}
.quick li::before{content:"›";margin-right:6px}
.newsletter{position:absolute;left:766px;top:82px;width:262px}
.newsletter .input{margin-top:22px;height:36px;background:var(--white);border-radius:2px;font-size:12px;color:#7a7f8c;display:flex;align-items:center;padding-left:12px}
.newsletter .send{margin-top:7px;height:38px;background:var(--blue);color:var(--white);font-family:"Oswald",sans-serif;font-size:14px;display:flex;align-items:center;justify-content:center;border-radius:2px}
.copyright{position:absolute;left:0;width:1200px;top:356px;text-align:center;color:#d6d9e2;font-size:12.5px}
</style>
</head>
<body>

<header class="hero">
  <div class="hero-photo" role="img" aria-label="Photo of a young woman in headphones writing lyrics at a guitar beside a studio microphone" style="position:absolute;inset:0"></div>
  <div class="brand">BAC<span class="mark"></span></div>
  <nav class="nav"><span>Home</span><span>Out Staff</span><span>Launch Your Music</span><span>FAQ</span><span>Artist Profiles</span></nav>
  <div class="social" aria-label="Social links"><span></span><span></span><span></span><span></span></div>
  <h1 class="hero-title heading">All Original Artists-All Original Country</h1>
  <p class="hero-tag">24/7, COMMERCIAL FREE, ALL THE TIME</p>
  <a class="btn">Know More <svg width="10" height="10" viewBox="0 0 10 10"><path d="M2 1l6 4-6 4z" fill="none" stroke="#fff" stroke-width="1.3"/></svg></a>
  <div class="dots"><span class="on"></span><span></span><span></span><span></span></div>
</header>

<section class="welcome">
  <div class="welcome-art" role="img" aria-label="Network initials artwork combined with a smiling woman in headphones and a studio microphone"></div>
  <div class="welcome-text">
    <p class="eyebrow">WELCOME TO</p>
    <h2 class="welcome-title heading">Balladcraft Airwave<br>Circle <span>(BAC)</span></h2>
    <p class="lead">In the 1990’s, the music industry imploded with the closing of large recording studios. At the same time, with the dawning of digital home studios, the number of solid songwriting artists exploded</p>
    <a class="btn">Read More <svg width="10" height="10" viewBox="0 0 10 10"><path d="M2 1l6 4-6 4z" fill="none" stroke="#fff" stroke-width="1.3"/></svg></a>
  </div>
</section>

<section class="partners">
  <h2 class="heading">Music <b>Partners</b></h2>
  <div class="partner-row" aria-label="Partner badges">
    <span></span><span class="round"></span><span></span><span></span><span class="round"></span><span></span>
  </div>
</section>

<section class="exposure">
  <div class="exposure-art" role="img" aria-label="Young man seated on a tall stool playing an acoustic guitar"></div>
  <h2 class="heading">Get over 4<sup>1/2</sup> hours of<br>exposure per month</h2>
  <p class="sub">RIGHT NOW, <b>FOR FREE</b></p>
  <ul class="points">
    <li>BAC provide you and your songs with international exposure.</li>
    <li>We are truly dedicated to getting your music out and your success.</li>
    <li>Artists receive 10 uninterrupted minutes of airtime EVERY DAY for 28 days. (This free offer to you may last longer)</li>
    <li>Artists will be given a schedule and link to your show to share on social media.</li>
  </ul>
</section>

<section class="how">
  <h2 class="heading">How it works</h2>
  <div class="steps">
    <div class="step one">
      <div class="step-accent"></div>
      <div class="step-card">
        <div class="step-icon" role="img" aria-label="Music notes icon"></div>
        Submit 2 songs for review. If they are accepted, we want you to create an audio recording of your voice, giving our listeners a quick background on yourself, a little info about the songs and where people can find you and buy your music. (Don't worry, we will send you a form to read and record yourself where you'll just fill in the blanks about you and your songs). BAC takes care of the rest.
      </div>
      <div class="step-tab">STEP <b>01</b></div>
    </div>
    <div class="step two">
      <div class="step-accent"></div>
      <div class="step-card">
        <div class="step-icon" role="img" aria-label="Song sheet icon"></div>
        One of our international DJs will receive your two songs and audio file in your own voive. Our radio DJ will create a custom 10-minute feature, all about you, your songs and where listeners can find you and purchase your music.
      </div>
      <div class="step-tab">STEP <b>02</b></div>
    </div>
    <div class="step three">
      <div class="step-accent"></div>
      <div class="step-card">
        <div class="step-icon" role="img" aria-label="Guitar player icon"></div>
        BAC doed not recieve any commission on your sales. Those are your sales.<br><br>What if this exposure lands you a contract with a label or publisher? Great!! (We don't want a piece of that either.)
      </div>
      <div class="step-tab">STEP <b>03</b></div>
    </div>
  </div>
</section>

<section class="artists">
  <h2 class="heading">Artist Profiles</h2>
  <div class="artist-row">
    <div class="artist">
      <div class="artist-photo" role="img" aria-label="Portrait of a smiling man in a blue blazer"></div>
      <div class="artist-info"><h3>Marco Vell</h3><p>Singer</p></div>
    </div>
    <div class="artist">
      <div class="artist-photo" role="img" aria-label="Portrait of a bearded man in glasses"></div>
      <div class="artist-info"><h3>Tobin Ashe</h3><p>Songwriter</p></div>
    </div>
    <div class="artist">
      <div class="artist-photo" role="img" aria-label="Portrait of a smiling woman with long dark hair"></div>
      <div class="artist-info"><h3>Rhea Calloway</h3><p>Rapper</p></div>
    </div>
  </div>
</section>

<section class="faq">
  <h2 class="heading">FAQ</h2>
  <div class="faq-grid">
    <div class="faq-item">Q. Are you a compelling singer/songwriter?</div>
    <div class="faq-item">Q. Do you have CDs, LPs or downloads to sell?</div>
    <div class="faq-item">Q. Have you written some really strong country songs that you feel could rival the big artists?</div>
    <div class="faq-item">Q. Would you be okay with international exposure?</div>
    <div class="faq-item">Q. Do you want to expand your fan base?</div>
    <div class="faq-item">Q. Are you frustrated trying to get the exposure you deserve?</div>
  </div>
</section>

<footer class="footer">
  <div class="brand">BAC<span class="mark"></span></div>
  <div class="social" aria-label="Social links"><span></span><span></span><span></span><span></span></div>
  <div class="divider" style="left:443px"></div>
  <div class="quick">
    <p class="col-title">QUICK LINKS</p>
    <ul><li>Home</li><li>Out Staff</li><li>Launch Your Music</li><li>FAQ</li><li>Artist Profiles</li></ul>
  </div>
  <div class="divider" style="left:721px"></div>
  <div class="newsletter">
    <p class="col-title">NEWSLETTER</p>
    <div class="input">✉&nbsp; Enter Email Address</div>
    <div class="send">SUBSCRIBE</div>
  </div>
  <p class="copyright">© 2022 <b>BAC</b>. All right reserved</p>
</footer>

</body>
</html>
```